Marlow Ridge Dental business card

Business card would have following info:

Alden R. Kasprzak, DMD, FAGD
General Dentist
email: office@marlowridgedental.example
phone: 617-490-3867
fax: 617-490-3867
website: marlowridgedental.example

second side would have lines for:

appointment date
appointment time

```html
<!DOCTYPE html>
<html lang="en">
<head>
<meta charset="utf-8">
<title>Marlow Ridge Dental – Appointment Card</title>
<link rel="stylesheet" href="https://fonts.googleapis.com/css2?family=Montserrat:wght@300;600&display=swap">
<style>
  :root {
    --card-blue: #52b1d3;
    --pattern-blue: #5ab7d6;
    --pattern-pink: #f2a0a8;
    --ink-white: #ffffff;
  }
  html, body {
    margin: 0;
    padding: 0;
    width: 1200px;
    height: 698px;
    overflow: hidden;
    background: var(--card-blue);
  }
  .card {
    position: relative;
    width: 1200px;
    height: 698px;
    overflow: hidden;
    font-family: "Montserrat", Arial, sans-serif;
    color: var(--ink-white);
  }
  .tooth-pattern {
    position: absolute;
    inset: 0;
    background:
      radial-gradient(circle at 30% 40%, rgba(242,160,168,0.18), transparent 60%),
      radial-gradient(circle at 75% 70%, rgba(242,160,168,0.16), transparent 55%),
      var(--pattern-blue);
  }
  .appointment-panel {
    position: absolute;
    left: 276px;
    top: 173px;
    width: 648px;
    height: 357px;
    background: var(--card-blue);
  }
  .appointment-title {
    position: absolute;
    left: 329px;
    top: 227px;
    margin: 0;
    font-size: 40px;
    font-weight: 600;
    letter-spacing: 0.2px;
    white-space: nowrap;
  }
  .appointment-field {
    position: absolute;
    left: 329px;
    display: flex;
    align-items: flex-end;
    font-size: 40px;
    font-weight: 300;
    line-height: 1;
  }
  .appointment-field.date { top: 323px; }
  .appointment-field.time { top: 413px; }
  .field-line {
    display: inline-block;
    width: 418px;
    height: 0;
    border-bottom: 2px solid var(--ink-white);
    margin-left: 4px;
    margin-bottom: 2px;
  }
  .dental-probe {
    position: absolute;
    left: 128px;
    top: 0;
    width: 86px;
    height: 404px;
    background: linear-gradient(90deg, var(--ink-white) 0 36px, transparent 36px);
    border-radius: 0 0 8px 8px;
    opacity: 0.95;
  }
  .dental-mirror {
    position: absolute;
    left: 950px;
    top: 384px;
    width: 110px;
    height: 314px;
    background: var(--ink-white);
    border-radius: 55px 55px 0 0;
    opacity: 0.95;
  }
</style>
</head>
<body>
  <main class="card">
    <div class="tooth-pattern" role="img" aria-label="Repeating pattern of light blue teeth with pink rings"></div>
    <div class="dental-probe" role="img" aria-label="White dental probe illustration"></div>
    <div class="dental-mirror" role="img" aria-label="White dental mirror illustration"></div>
    <section class="appointment-panel" aria-hidden="true"></section>
    <h1 class="appointment-title">Your Next Appointment</h1>
    <div class="appointment-field date"><span>Date:</span><span class="field-line"></span></div>
    <div class="appointment-field time"><span>Time:</span><span class="field-line"></span></div>
  </main>
</body>
</html>
```